Campaign Flyer for a local election

Black and white election flyer

See information below to be included:

Re-elect Morton
Experienced Glenmoor Board Member
Experienced NYC Principal
Experienced leader

One Year Board Accomplishments:
-Installed New Park Lights (Bollards)
-Red Brick Road Repair Project
-Established Closer Ties with Our local precinct to frequently monitor the community with directed security patrols. Requested an increased police presence.
-Met with the 82nd Precinct Officials & Assemblywoman, Linda Marwick to discuss our security issues
- Focused on maintenance of streetlights to make brighter streets
-Negotiated Contract & Hired Our New Landscaper, Hollowfield Landscapers
-Major Homeowner Shrub Replacement Project
- Addressing Standing Water in our Park (Installed French Drain)
- Replaced and upgraded all 5 outdoor circuit breaker panels
-Write monthly community newsletters
-Sewer cleaning project (had all community catch basins cleaned)
-Carefully overseeing our new school project. Coordinating with the sponsor and the school directors
-Delivered a very healthy budget to the community
-Works closely with our committees
-Events: Zoo event, Petting Zoo, Outdoor Movie Night, Egg Hunt

It is my intent to seek re-election.
(Photo) Morton Velasquez
-Dedicated to improving our community
-Hard-working…He gets thing done!
-Trustworthy

. .

Please note, I am submitting new information under accomplishments. The list of accomplishments should be in the same sequence, starting with: Met with the 82nd Precinct....
Please carefully review.
----------------------------------------------------------------------------------------------------------------------------------------------------------------

Re-elect Morton
Experienced NYC Principal
Experienced leader

Last Year’s Board Accomplishments:

-Met with the 82nd Precinct Officials & Assemblywoman, Linda Marwick, to discuss our security issues. Requested increased police presence.
-Established a strong partnership with the 82nd precinct to frequently monitor the community with directed security patrols.
-Replaced all new park lights (Bollards) to make the park brighter
- Focused on maintenance of streetlights to make streets brighter
-‘Fixing Our Streets Project’ (Repaired all cracked/missing red bricks)
-Homeowner Shrub Replacement Project (Replaced hundreds of bushes)
- I write the monthly community newsletter
-Carefully overseeing our new school project. Coordinating with the sponsor and the school director
-Monitoring C of O’s and homeowners Insurance

(Photo) Morton Velasquez
-Hard-working! I get things done!
-Trustworthy

. .

Re-elect Morton
Experienced NYC Principal
Experienced leader

(Photo) Morton Velasquez
-Trustworthy

. .

Target Market(s)

A Community electing a Board Member

Industry/Entity Type

residential election

Requirements
Must have
• all black, white and grey print. Flyers will not be printed in color
Nice to have
• See the information in the attachment below containing all my accomplishments
Should not have
• color

```html
<!DOCTYPE html>
<html lang="en">
<head>
<meta charset="utf-8">
<title>Re-elect Morton</title>
<link rel="stylesheet" href="https://fonts.googleapis.com/css2?family=Source+Sans+3:wght@400;700;800&display=swap">
<style>
  :root {
    --ink: #111111;
    --band: #000000;
    --paper: #ffffff;
    --photo-tone-a: #d9d9d9;
    --photo-tone-b: #4a4a4a;
  }
  * { margin: 0; padding: 0; box-sizing: border-box; }
  html, body { width: 848px; height: 1200px; overflow: hidden; background: var(--paper); }
  .flyer {
    position: relative;
    width: 848px;
    height: 1200px;
    overflow: hidden;
    background: var(--paper);
    color: var(--ink);
    font-family: "Source Sans 3", "Myriad Pro", Arial, sans-serif;
  }
  .flyer-frame { position: absolute; inset: 0; }
  .headline {
    position: absolute;
    top: 52px;
    left: 0;
    width: 848px;
    text-align: center;
    font-size: 66px;
    font-weight: 800;
    letter-spacing: 9px;
    line-height: 1;
    padding-left: 9px;
  }
  .credentials {
    position: absolute;
    top: 208px;
    left: 35px;
    color: var(--paper);
    font-size: 27px;
    font-weight: 700;
    line-height: 34px;
  }
  .accomplishments-title {
    position: absolute;
    top: 330px;
    left: 35px;
    font-size: 37px;
    font-weight: 400;
    line-height: 1.1;
    letter-spacing: -0.3px;
    padding-bottom: 2px;
    border-bottom: 2px solid var(--ink);
    width: 639px;
  }
  .accomplishments {
    position: absolute;
    top: 380px;
    left: 35px;
    width: 790px;
    list-style: none;
    font-size: 18px;
    line-height: 23.8px;
  }
  .accomplishments li { padding-left: 9px; text-indent: -9px; }
  .candidate-box {
    position: absolute;
    top: 822px;
    left: 0;
    width: 848px;
    height: 340px;
    border: 2px solid var(--ink);
    border-bottom: none;
  }
  .intent {
    position: absolute;
    top: 840px;
    left: 0;
    width: 848px;
    text-align: center;
    font-size: 38px;
    font-weight: 800;
    line-height: 1.2;
  }
  .portrait {
    position: absolute;
    top: 903px;
    left: 34px;
    width: 154px;
    height: 202px;
    background: linear-gradient(180deg, var(--photo-tone-a) 0%, #9a9a9a 55%, var(--photo-tone-b) 100%);
    border: 1px solid #888;
  }
  .candidate-name {
    position: absolute;
    top: 896px;
    left: 199px;
    font-size: 64px;
    font-weight: 800;
    line-height: 1.1;
    letter-spacing: -0.5px;
    white-space: nowrap;
  }
  .name-rule {
    position: absolute;
    top: 981px;
    left: 205px;
    width: 577px;
    height: 2px;
    background: var(--ink);
  }
  .qualities {
    position: absolute;
    top: 994px;
    left: 200px;
    list-style: none;
    font-size: 30px;
    font-weight: 700;
    line-height: 39px;
  }
</style>
</head>
<body>
<main class="flyer">
  <svg class="flyer-frame" width="848" height="1200" viewBox="0 0 848 1200" aria-hidden="true">
    <rect x="0" y="0" width="848" height="9" fill="var(--band)"/>
    <path d="M569 0 H848 V43 H600 Q590 43 585 35 Z" fill="var(--band)"/>
    <path d="M0 146 H250 Q260 146 265 154 L277 179 H848 V189 H0 Z" fill="var(--band)"/>
    <rect x="0" y="189" width="848" height="133" fill="var(--band)"/>
    <path d="M0 1157 H217 Q225 1147 240 1147 H604 Q619 1147 627 1157 H848 V1200 H0 Z" fill="var(--band)"/>
  </svg>

  <h1 class="headline">RE-ELECT MORTON</h1>

  <div class="credentials">
    <p>Experienced Glenmoor Board Member</p>
    <p>Experienced NYC Principal</p>
    <p>Experienced leader</p>
  </div>

  <h2 class="accomplishments-title">ONE YEAR BOARD ACCOMPLISHMENTS :</h2>
  <ul class="accomplishments">
    <li>- Installed New Park Lights (Bollards)</li>
    <li>- Red Brick Road Repair Project</li>
    <li>- Established Closer Ties with Our local precinct to frequently monitor the community with<br>directed security patrols. Requested an increased police presence.</li>
    <li>- Met with the 82nd Precinct Officials &amp; Assemblywoman, Linda Marwick to discuss our security<br>issues</li>
    <li>- Focused on maintenance of streetlights to make brighter streets</li>
    <li>- Negotiated Contract &amp; Hired Our New Landscaper, Hollowfield Landscapers</li>
    <li>- Major Homeowner Shrub Replacement Project</li>
    <li>- &nbsp;Addressing Standing Water in our Park (Installed French Drain)</li>
    <li>- &nbsp;Replaced and upgraded all 5 outdoor circuit breaker panels</li>
    <li>- Write monthly community newsletters</li>
    <li>- Sewer cleaning project (had all community catch basins cleaned)</li>
    <li>- Carefully overseeing our new school project. Coordinating with the sponsor and the school<br>directors</li>
    <li>- Delivered a very healthy budget to the community</li>
    <li>- Works closely with our committees</li>
    <li>- Events: Zoo event, Petting Zoo, Outdoor Movie Night, Egg Hunt</li>
  </ul>

  <section class="candidate-box" aria-label="Candidate">
  </section>
  <h2 class="intent">IT IS MY INTENT TO SEEK RE-ELECTION</h2>
  <div class="portrait" role="img" aria-label="Black and white portrait photo of candidate Morton Velasquez"></div>
  <h3 class="candidate-name">MORTON VELASQUEZ</h3>
  <div class="name-rule"></div>
  <ul class="qualities">
    <li>- Dedicated to improving our community</li>
    <li>- Hard-working…He gets thing done!</li>
    <li>- Trustworthy</li>
  </ul>
</main>
</body>
</html>
```